Real Estate Development Company Stationary

We need our company, business card, letterhead, pocket folder and envelope designed.

We are a new real estate development company. We focus on data centre, commercial and real estate development.

Please see attached for our logo. Since it's a new logo, you still can make minor adjust if you like it makes senses

The client has sent me a business card he really likes. Please see file 3.

Target Market(s)

Real Estate Investors
Large corporations
Home buyers

Industry/Entity Type

Real Estate

```html
<!DOCTYPE html>
<html lang="en">
<head>
<meta charset="utf-8">
<title>Quellmont Properties — Stationery</title>
<link href="https://fonts.googleapis.com/css2?family=Arimo:wght@400;700&display=swap" rel="stylesheet">
<style>
  :root {
    --blue: #0d4a8f;
    --blue-deep: #083a73;
    --green: #5bb53a;
    --paper: #ffffff;
    --ink: #3a3f47;
    --ink-soft: #6b717a;
    --backdrop: #737985;
    --backdrop-dark: #5f6570;
  }
  * { box-sizing: border-box; margin: 0; padding: 0; }
  html, body { width: 1200px; height: 863px; overflow: hidden; }
  body {
    position: relative;
    background: linear-gradient(180deg, var(--backdrop-dark), var(--backdrop));
    font-family: "Arimo", Arial, sans-serif;
    color: var(--ink);
  }
  .sheet { position: absolute; box-shadow: 0 6px 18px rgba(0,0,0,.25); }

  .brand { display: flex; align-items: center; gap: 6px; color: var(--green); font-weight: 700; white-space: nowrap; }
  .brand-dot { width: .9em; height: .9em; border-radius: 50%; background: var(--blue); flex: none; }

  /* Envelope back */
  .envelope-back { left: 140px; top: 80px; width: 500px; height: 250px; background: var(--blue); overflow: hidden; }
  .envelope-back svg { position: absolute; right: 0; top: 0; }

  /* Envelope front */
  .envelope-front { left: 80px; top: 210px; width: 500px; height: 250px; background: var(--paper); }
  .envelope-front .brand { position: absolute; left: 22px; top: 20px; font-size: 15px; }
  .envelope-front .divider-v { position: absolute; left: 170px; top: 0; bottom: 0; width: 1px; background: var(--blue); }
  .envelope-front .divider-h { position: absolute; left: 0; top: 150px; width: 170px; height: 1px; background: var(--blue); }
  .envelope-front .sender { position: absolute; left: 22px; top: 52px; font-size: 8px; line-height: 1.5; color: var(--blue); }

  /* Business card front */
  .card-front { left: 80px; top: 590px; width: 260px; height: 150px;
    background: linear-gradient(135deg, var(--blue) 35%, var(--green));
    display: flex; align-items: center; justify-content: center; }
  .card-front .brand { color: var(--paper); font-size: 24px; }
  .card-front .brand-dot { background: var(--paper); }

  /* Business card back */
  .card-back { left: 370px; top: 590px; width: 260px; height: 150px; background: var(--paper); overflow: hidden; border-bottom: 8px solid var(--blue); }
  .card-back .brand { position: absolute; left: 18px; top: 16px; font-size: 14px; }
  .card-back .corner { position: absolute; right: 0; bottom: 30px; width: 36px; height: 24px; background: var(--green); }
  .card-back .holder { position: absolute; right: 50px; top: 62px; text-align: right; }
  .card-back .holder-name { font-size: 13px; font-weight: 700; color: var(--blue); }
  .card-back .holder-role { font-size: 8px; color: var(--ink-soft); margin-top: 2px; }
  .card-back .contact { position: absolute; left: 18px; bottom: 12px; font-size: 7.5px; line-height: 1.5; color: var(--blue); }

  /* Pocket folder */
  .folder { left: 725px; top: 150px; width: 430px; height: 640px; background: var(--blue); }

  /* Letterhead */
  .letterhead { left: 690px; top: 110px; width: 420px; height: 594px; background: var(--paper); padding: 0 40px; }
  .letterhead .brand { position: absolute; right: 36px; top: 44px; font-size: 22px; }
  .letterhead .body { position: absolute; left: 40px; right: 40px; top: 120px; font-size: 8.5px; line-height: 1.55; color: var(--ink-soft); }
  .letterhead .body p + p { margin-top: 10px; }
  .letterhead .signature { position: absolute; left: 40px; top: 300px; }
  .letterhead .signature-name { font-size: 11px; color: var(--ink); }
  .letterhead .signature-role { font-size: 7.5px; color: var(--ink-soft); margin-top: 3px; }
  .letterhead .footer-rule { position: absolute; left: 0; right: 0; bottom: 80px; height: 1px; background: var(--blue); }
  .letterhead .footer { position: absolute; left: 40px; bottom: 38px; font-size: 7.5px; line-height: 1.5; color: var(--blue); }
</style>
</head>
<body>

  <div class="sheet envelope-back">
    <svg width="140" height="250" viewBox="0 0 140 250" aria-hidden="true">
      <polygon points="0,0 140,0 140,250 0,250 110,125" fill="var(--green)"/>
    </svg>
  </div>

  <div class="sheet envelope-front">
    <div class="brand"><span class="brand-dot"></span>Quellmont Properties</div>
    <div class="sender">12 Harbour Street, Suite 400<br>Toronto, ON M5J 2L1</div>
    <div class="divider-v"></div>
    <div class="divider-h"></div>
  </div>

  <div class="sheet card-front">
    <div class="brand"><span class="brand-dot"></span>Quellmont</div>
  </div>

  <div class="sheet card-back">
    <div class="brand"><span class="brand-dot"></span>Quellmont Properties</div>
    <div class="holder">
      <div class="holder-name">Lena Moreau</div>
      <div class="holder-role">Project Director</div>
    </div>
    <div class="corner"></div>
    <div class="contact">T 416 555 0190<br>lena@quellmontprop.com</div>
  </div>

  <div class="sheet folder"></div>

  <div class="sheet letterhead">
    <div class="brand"><span class="brand-dot"></span>Quellmont Properties</div>
    <div class="body">
      <p>Lorem ipsum dolor sit amet, consectetur adipiscing elit. Donec nisi purus, luctus vitae dignissim eu, iaculis sed purus. Vivamus facilisis, ipsum nec aliquet viverra, leo mauris vestibulum turpis, vel semper lorem quam eget velit. Sed quis nunc at risus fermentum.</p>
      <p>Quisque commodo mollis nulla at porttitor. Mauris a tortor id tellus interdum tristique. Sed ut augue vitae arcu ultricies aliquet. Praesent sed justo in mi dictum tempus. Aenean ac ligula vel erat elementum placerat in vitae lectus.</p>
    </div>
    <div class="signature">
      <div class="signature-name">Daniel Hartley</div>
      <div class="signature-role">Co-Founder &amp; CEO</div>
    </div>
    <div class="footer-rule"></div>
    <div class="footer">T 416 555 0182 &nbsp; F 416 555 0183<br>info@quellmontprop.com<br>www.quellmontprop.com</div>
  </div>

</body>
</html>
```